Brindle Logistics Business Card Design

We are a trucking and warehousing company. We run freight in the US manly from the Pacific NW to TX and back up the the PNW. We also do warehousing where we store, move, and distribute freight. Looking for a clean and modern design of business card. We would like to look rich and elegant. Attached is our logo.

Industry/Entity Type

Trucking Company

Contact Information for Business Card

Looking for a clean and modern design of business card. We would like to look rich and elegant.

Font styles to use
Sans Serif

Colors

Designer to choose colors to be used in the design.

Requirements
Must have
• logo but it should not dominate the card
Should not have
• logo should not dominate the card

```html
<!DOCTYPE html>
<html lang="en">
<head>
<meta charset="utf-8">
<title>Brindle Logistics Business Card</title>
<link href="https://fonts.googleapis.com/css2?family=Mulish:wght@400;600;700&display=swap" rel="stylesheet">
<style>
  :root {
    --backdrop: #2e2e2e;
    --card: #ffffff;
    --brand-blue: #0a6cb5;
    --brand-blue-soft: #86bde3;
    --brand-orange: #f39c12;
    --brand-orange-soft: #f9cd8f;
    --ink: #3d3d3d;
    --ink-light: #555555;
  }
  * { box-sizing: border-box; margin: 0; padding: 0; }
  html, body {
    width: 1200px; height: 1200px; overflow: hidden;
    background: var(--backdrop);
    font-family: "Mulish", sans-serif;
  }
  .canvas { position: relative; width: 1200px; height: 1200px; }
  .card {
    position: absolute; left: 329px; width: 542px; height: 320px;
    background: var(--card); overflow: hidden;
  }
  .card--front { top: 223px; }
  .card--back { top: 640px; }

  .brand {
    position: absolute; display: flex; align-items: center; gap: 10px;
    color: var(--brand-blue); font-weight: 700; line-height: 1.05;
  }
  .brand__mark { width: 14px; height: 14px; background: var(--brand-blue); flex: none; }
  .brand__name { font-size: 22px; letter-spacing: 0.5px; }
  .card--front .brand { left: 24px; top: 38px; }
  .card--back .brand { left: 313px; top: 50px; }

  .brand-art { position: absolute; }
  .card--front .brand-art {
    left: 271px; top: 28px; width: 271px; height: 292px;
    background: linear-gradient(135deg, var(--brand-orange) 0%, var(--brand-blue) 35%, var(--brand-blue) 100%);
    border-top-left-radius: 60% 40%;
  }
  .card--back .brand-art {
    left: 333px; top: 144px; width: 209px; height: 176px;
    background: linear-gradient(135deg, var(--brand-orange-soft) 0%, var(--brand-blue-soft) 35%, var(--brand-blue-soft) 100%);
    border-top-left-radius: 60% 40%;
  }

  .person { position: absolute; left: 32px; top: 50px; }
  .person__name { font-size: 27px; font-weight: 700; color: var(--ink); }
  .person__role { font-size: 17px; color: var(--brand-blue); margin: 6px 0 0 12px; }

  .contact { position: absolute; left: 31px; top: 150px; list-style: none; }
  .contact__item {
    display: flex; align-items: flex-start; gap: 10px;
    font-size: 14px; color: var(--ink-light); line-height: 18px; margin-bottom: 1px;
  }
  .contact__icon { width: 13px; height: 13px; flex: none; margin-top: 2px; }
  .contact__item--address { margin-bottom: 0; }
</style>
</head>
<body>
<main class="canvas">

  <section class="card card--front">
    <div class="brand">
      <span class="brand__mark"></span>
      <span class="brand__name">Brindle<br>Logistics, LLC</span>
    </div>
    <div class="brand-art" role="img" aria-label="Large brand emblem decoration in blue and orange"></div>
  </section>

  <section class="card card--back">
    <div class="person">
      <h1 class="person__name">John Doe</h1>
      <p class="person__role">CEO / Founder</p>
    </div>

    <div class="brand">
      <span class="brand__mark"></span>
      <span class="brand__name">Brindle<br>Logistics, LLC</span>
    </div>

    <ul class="contact">
      <li class="contact__item contact__item--address">
        <svg class="contact__icon" viewBox="0 0 12 12"><path d="M6 0.5a4 4 0 0 1 4 4c0 3-4 7-4 7s-4-4-4-7a4 4 0 0 1 4-4z" fill="#f39c12"/><circle cx="6" cy="4.5" r="1.5" fill="#fff"/></svg>
        <span>Full Address, FA 01<br>City Country, Zip code</span>
      </li>
      <li class="contact__item">
        <svg class="contact__icon" viewBox="0 0 12 12"><circle cx="6" cy="6" r="6" fill="#f39c12"/><path d="M4 3.2l1.2 1.4-.6.8c.4.8 1 1.4 1.8 1.8l.8-.6 1.4 1.2-.8 1c-2.4-.4-4.2-2.2-4.6-4.6z" fill="#fff"/></svg>
        <span>(00) xxxx-xxxx</span>
      </li>
      <li class="contact__item">
        <svg class="contact__icon" viewBox="0 0 12 12"><circle cx="6" cy="6" r="6" fill="#f39c12"/><rect x="4" y="2.8" width="4" height="6.4" rx="0.8" fill="#fff"/><rect x="4.7" y="3.6" width="2.6" height="4" fill="#f39c12"/></svg>
        <span>(+00) xxx-xxxx-xx</span>
      </li>
      <li class="contact__item">
        <svg class="contact__icon" viewBox="0 0 12 12"><circle cx="6" cy="6" r="6" fill="#f39c12"/><rect x="3" y="4" width="6" height="4.2" fill="#fff"/><path d="M3 4l3 2.2L9 4" stroke="#f39c12" stroke-width="0.8" fill="none"/></svg>
        <span>johnd@brindlelogisticsllc.com</span>
      </li>
      <li class="contact__item">
        <svg class="contact__icon" viewBox="0 0 12 12"><circle cx="6" cy="6" r="5.2" fill="none" stroke="#f39c12" stroke-width="1.2"/><ellipse cx="6" cy="6" rx="2.2" ry="5.2" fill="none" stroke="#f39c12" stroke-width="0.9"/><path d="M1 6h10" stroke="#f39c12" stroke-width="0.9"/></svg>
        <span>brindlelogisticsllc.com</span>
      </li>
    </ul>

    <div class="brand-art" role="img" aria-label="Faint brand emblem decoration in light blue and peach"></div>
  </section>

</main>
</body>
</html>
```